Covid 19 Exit Strategy one page brochure

I would like to design, and will need URGENT help, a brochure detailing a Covid 19 Exit Strategy plan. This brochure will need to be understood easily and the graphics inside should make it easy for people to understand without reading the entire text. This project is quite urgent and needs to be completed THIS WEEK - by Saturday may 16th at the latest. I am attaching two examples. I will provide the text.

```html
<!DOCTYPE html>
<html lang="en">
<head>
<meta charset="utf-8">
<title>Covid-19 Phased Exit Strategy</title>
<link rel="stylesheet" href="https://fonts.googleapis.com/css2?family=Montserrat:wght@400;500;600;700;800&display=swap">
<style>
  :root {
    --backdrop: #ececec;
    --page-blue: #3a9fe6;
    --page-blue-light: #5bb5f0;
    --page-blue-deep: #2a8bd8;
    --particle: #2f86d2;
    --navy: #12335c;
    --white: #ffffff;
    --photo-light: #eef5f9;
    --photo-mid: #bcd8ec;
  }
  * { box-sizing: border-box; margin: 0; padding: 0; }
  html, body { width: 1200px; height: 1200px; overflow: hidden; }
  body {
    background: var(--backdrop);
    font-family: "Montserrat", Arial, sans-serif;
    color: var(--navy);
  }
  .brochure {
    position: absolute;
    left: 204px; top: 40px;
    width: 792px; height: 1120px;
    background: var(--page-blue);
    overflow: hidden;
    box-shadow: 0 2px 10px rgba(0,0,0,.12);
  }
  .brochure__backdrop { position: absolute; inset: 0; width: 100%; height: 100%; }
  .particle { fill: var(--particle); opacity: .75; }
  .content { position: relative; padding: 26px 40px 0; }

  .masthead { text-align: center; }
  .masthead__title {
    font-size: 46px; font-weight: 800; letter-spacing: 0.5px;
    color: var(--navy); line-height: 1;
  }
  .masthead__subtitle {
    font-size: 21px; font-weight: 700; color: var(--white);
    margin-top: 4px; line-height: 1.1;
  }
  .masthead__credit {
    font-size: 8px; font-weight: 700; letter-spacing: 1.4px;
    text-transform: uppercase; margin-top: 8px;
  }
  .intro {
    font-size: 8.4px; line-height: 11px; font-weight: 500;
    margin-top: 12px; text-align: justify;
  }

  .requirements { margin-top: 10px; }
  .requirements__heading {
    text-align: center; font-size: 11px; font-weight: 700; margin-bottom: 10px;
  }
  .requirements__grid {
    display: grid; grid-template-columns: 1fr 1fr; column-gap: 46px;
    padding: 0 20px;
  }
  .requirements__col { display: flex; flex-direction: column; gap: 11px; }
  .requirement {
    display: flex; align-items: center; gap: 12px;
    font-size: 8.4px; line-height: 11px; font-weight: 500;
  }
  .requirement__icon {
    flex: 0 0 26px; height: 26px;
    border: 2px solid var(--navy); border-radius: 7px;
    background: var(--page-blue-light);
  }

  .plan-heading {
    display: flex; align-items: center; gap: 14px;
    margin-top: 16px;
  }
  .plan-heading::before, .plan-heading::after {
    content: ""; flex: 1; height: 1px; background: var(--navy);
  }
  .plan-heading__text {
    font-size: 12px; font-weight: 800; color: var(--white);
    text-transform: uppercase; letter-spacing: 0.3px;
  }
  .plan-intro {
    font-size: 8.4px; line-height: 11px; font-weight: 500; margin-top: 8px;
  }

  .stages {
    display: grid; grid-template-columns: 1fr 1fr; column-gap: 30px;
    margin-top: 8px;
  }
  .stage__title {
    font-size: 13px; font-weight: 800; color: var(--white);
    margin: 6px 0 5px;
  }
  .stage__note { font-size: 8.2px; line-height: 10.6px; font-weight: 500; margin-bottom: 3px; }
  .stage__list { list-style: none; }
  .stage__list li {
    font-size: 8.2px; line-height: 10.6px; font-weight: 500; margin-bottom: 1px;
  }
  .stage__list b { font-weight: 800; margin-right: 3px; }
  .stages__spacer { height: 32px; }
  .stage--third { width: 290px; }

  .wash-photo {
    position: absolute; right: 0; bottom: 0;
    width: 180px; height: 132px;
    border-top-left-radius: 60px;
    background: linear-gradient(135deg, var(--photo-light) 0%, var(--photo-mid) 100%);
  }
</style>
</head>
<body>
<article class="brochure">
  <svg class="brochure__backdrop" viewBox="0 0 792 1120" aria-hidden="true">
    <path d="M0 0 H792 V118 C700 150 620 108 520 122 C420 138 330 168 220 150 C140 136 60 160 0 176 Z" fill="#5bb5f0"/>
    <path d="M0 0 H210 C190 40 140 60 90 62 C50 64 20 88 0 110 Z" fill="#2a8bd8"/>
    <path d="M792 1120 H560 C600 1080 640 1040 700 1010 C740 990 770 960 792 930 Z" fill="#2a8bd8" opacity=".5"/>
  </svg>

  <svg class="brochure__backdrop" viewBox="0 0 792 1120" role="img" aria-label="Decorative virus particles">
    <circle class="particle" cx="735" cy="30" r="32"/>
    <circle class="particle" cx="56" cy="40" r="18"/>
    <circle class="particle" cx="760" cy="222" r="14"/>
    <circle class="particle" cx="750" cy="305" r="38"/>
    <circle class="particle" cx="20" cy="470" r="34"/>
    <circle class="particle" cx="770" cy="530" r="30"/>
    <circle class="particle" cx="730" cy="705" r="18"/>
    <circle class="particle" cx="766" cy="800" r="12"/>
    <circle class="particle" cx="26" cy="780" r="22"/>
    <circle class="particle" cx="30" cy="1050" r="30"/>
    <circle class="particle" cx="330" cy="1090" r="28"/>
    <circle class="particle" cx="460" cy="1100" r="20"/>
  </svg>

  <div class="content">
    <header class="masthead">
      <h1 class="masthead__title">Covid-19</h1>
      <p class="masthead__subtitle">Phased Exit Strategy</p>
      <p class="masthead__credit">Developed by Dana Whitfield</p>
    </header>

    <p class="intro">Pandemics have, historically, been fought and won through two paths: a vaccine or broad community immunity. While work on a vaccine moves forward, daily life cannot stay on hold indefinitely. This plan sets out a careful, staged route out of lockdown, guided by clear health measures. Each stage opens a little more of the economy and social life, and each step depends on the general requirements below being met and sustained over time.</p>

    <section class="requirements">
      <h2 class="requirements__heading">General requirements:</h2>
      <div class="requirements__grid">
        <div class="requirements__col">
          <div class="requirement"><span class="requirement__icon" role="img" aria-label="Icon of a falling chart"></span><p>Single digit downward trend of documented cases within the past 14 days.</p></div>
          <div class="requirement"><span class="requirement__icon" role="img" aria-label="Icon of a test tube"></span><p>Ability to screen and test symptomatic individuals within 24 hours, with testing capacity for at least 30% of the population within 3 months.</p></div>
          <div class="requirement"><span class="requirement__icon" role="img" aria-label="Icon of tracking a patient"></span><p>Ability to track and trace infected patients and contacts on a large scale, and to react quickly to any unusual trends or outbreaks.</p></div>
          <div class="requirement"><span class="requirement__icon" role="img" aria-label="Icon of a face mask"></span><p>Mandatory use of masks in all public areas and at work, with protective equipment for all healthcare and essential workers.</p></div>
        </div>
        <div class="requirements__col">
          <div class="requirement"><span class="requirement__icon" role="img" aria-label="Icon of a hospital"></span><p>Hospitals and the health care system are capable of treating patients without operating in a crisis mode.</p></div>
          <div class="requirement"><span class="requirement__icon" role="img" aria-label="Icon of an intensive care bed"></span><p>Ability to surge ICU capacity on a short notice, 24h.</p></div>
          <div class="requirement"><span class="requirement__icon" role="img" aria-label="Icon of a containment plan"></span><p>Plan in place to trigger regional or full-scale containment in case of sudden outbreaks.</p></div>
          <div class="requirement"><span class="requirement__icon" role="img" aria-label="Icon of a thermometer"></span><p>Mandatory daily checks of body temperature for everyone at the workplace or entering public areas.</p></div>
          <div class="requirement"><span class="requirement__icon" role="img" aria-label="Icon of a sanitizer bottle"></span><p>Mandatory sanitation in all places, with disinfectant available on a large scale.</p></div>
        </div>
      </div>
    </section>

    <h2 class="plan-heading"><span class="plan-heading__text">Phased Covid-19 Lockdown Exit Strategy Plan</span></h2>
    <p class="plan-intro">To enter this stage, in addition to the general requirements, the effective reproduction number (R) must be less than 1 and the death rate below 3%. The economy and social activities can resume in this sequence.</p>

    <section class="stages">
      <div class="stage stage--first">
        <h3 class="stage__title">STAGE 1:</h3>
        <ol class="stage__list">
          <li><b>1.</b>Elderly (65+) and vulnerable individuals should continue to self-isolate as much as possible.</li>
          <li><b>2.</b>No more than 5 people may gather, keeping at least 2 meters apart.</li>
          <li><b>3.</b>Work from home should continue wherever and as much as possible.</li>
          <li><b>4.</b>Social distancing should continue in all public areas, at work and at home.</li>
          <li><b>5.</b>Movement between cities and regions is allowed, with the same rules as before.</li>
          <li><b>6.</b>Large businesses (100 people and more, such as manufacturing and services) may run in rotating shifts of no more than 30% of staff.</li>
          <li><b>7.</b>Small businesses (50 people and less) can reopen at full capacity with safe working conditions.</li>
          <li><b>8.</b>Commercial shops may reopen with limited hours and checks at every entrance.</li>
          <li><b>9.</b>Pharmacies will continue to be open, with masks and gloves for all staff.</li>
        </ol>
      </div>
      <div class="stage stage--first-cont">
        <ol class="stage__list" style="margin-top:10px">
          <li><b>10.</b>Transportation (buses, taxis, airlines) will resume at half capacity, with all passengers wearing masks and vehicles cleaned between trips.</li>
          <li><b>11.</b>Religious sites can reopen with a maximum capacity of 30% and social distancing.</li>
          <li><b>12.</b>Hotels and tourism sites remain closed to visitors during this stage.</li>
          <li><b>13.</b>Coffee shops and restaurants can offer takeaway and delivery only.</li>
          <li><b>14.</b>All schools and universities remain closed, with learning continuing online.</li>
          <li><b>15.</b>Large public events such as concerts, sports and conferences remain cancelled.</li>
        </ol>
      </div>

      <div class="stage stage--second">
        <div class="stages__spacer"></div>
        <h3 class="stage__title">STAGE 2:</h3>
        <ol class="stage__list">
          <li><b>1.</b>Elderly and vulnerable individuals should still limit contact and stay home when possible.</li>
          <li><b>2.</b>Gatherings of up to 15 people are allowed in private settings.</li>
          <li><b>3.</b>Work from home is still encouraged for roles that allow it.</li>
          <li><b>4.</b>Elective surgeries resume in hospitals and clinics that meet safety rules.</li>
          <li><b>5.</b>Large businesses may raise staff on site to 60% in rotating shifts.</li>
          <li><b>6.</b>Commercial shops return to normal opening hours with entry limits.</li>
          <li><b>7.</b>Transportation runs at 75% capacity, with masks required on board.</li>
          <li><b>8.</b>Religious sites can open at 50% capacity with distancing in place.</li>
          <li><b>9.</b>Hotels and tourism sites reopen at 50% capacity for local visitors.</li>
          <li><b>10.</b>Coffee shops and restaurants open at 50% capacity, tables kept apart.</li>
          <li><b>11.</b>Schools plan a staged return with small classes and split timetables.</li>
          <li><b>12.</b>Large public events remain on hold until the next stage.</li>
        </ol>
      </div>
      <div class="stage stage--third">
        <div class="stages__spacer"></div>
        <h3 class="stage__title">STAGE 3:</h3>
        <p class="stage__note">To enter stage 3, the effective reproduction number must stay below 1 and no new clusters may appear for 28 days.</p>
        <ol class="stage__list">
          <li><b>1.</b>Elderly and vulnerable individuals may resume most daily activities with care.</li>
          <li><b>2.</b>Gatherings of up to 50 people are allowed with basic hygiene rules.</li>
          <li><b>3.</b>All hospital and clinic services return to normal operation.</li>
          <li><b>4.</b>Large and small businesses return to full staff on site.</li>
          <li><b>5.</b>Transportation returns to full capacity; masks remain advised.</li>
          <li><b>6.</b>Religious sites, hotels and tourism sites open at full capacity.</li>
          <li><b>7.</b>Coffee shops and restaurants resume normal service with hand sanitizer at every table.</li>
          <li><b>8.</b>Schools and universities reopen for all students.</li>
          <li><b>9.</b>Large public events may resume with temperature checks at entry.</li>
        </ol>
      </div>
    </section>
  </div>

  <div class="wash-photo" role="img" aria-label="Photo of hands being washed with soap and water"></div>
</article>
</body>
</html>
```